Building Company Business Card Design

Need a design for a business card:
It needs to have: Name, Phone, Facebook link, Website, email
i would also like a list of works we undertake:
-New Homes
-Extensions, Renovations & Bathrooms
-Decking, Carports, Sheds (Residential and Industrial)
-Carpentry
-Fences, Patios & Pergolas

Name, Phone, Facebook link, Website, email + details of services provided listed in description

```html
<!DOCTYPE html>
<html lang="en">
<head>
<meta charset="utf-8">
<title>Keystone Homes – Business Card</title>
<link href="https://fonts.googleapis.com/css2?family=Montserrat:wght@400;500;600;700&display=swap" rel="stylesheet">
<style>
  :root {
    --brand-green: #37b34a;
    --ink: #1c1c1c;
    --paper: #ffffff;
    --backdrop: #3a3a3a;
  }
  * { box-sizing: border-box; margin: 0; padding: 0; }
  html, body { width: 1200px; height: 1200px; overflow: hidden; }
  body {
    background: var(--backdrop);
    font-family: "Montserrat", sans-serif;
    position: relative;
  }
  .card {
    position: absolute;
    left: 170px;
    width: 860px;
    height: 491px;
    border-radius: 30px;
    overflow: hidden;
  }
  /* Services side */
  .card--services {
    top: 72px;
    background: var(--brand-green);
    color: var(--paper);
    text-align: center;
  }
  .services-brand {
    margin-top: 110px;
    font-weight: 700;
    font-size: 44px;
    line-height: 1.1;
    letter-spacing: 1px;
    text-transform: uppercase;
    display: flex;
    align-items: center;
    justify-content: center;
    gap: 16px;
  }
  .services-brand .mark {
    width: 30px; height: 30px; background: var(--paper);
  }
  .services-brand small { display: block; font-size: 44px; }
  .services-title {
    display: inline-block;
    margin-top: 34px;
    font-weight: 600;
    font-size: 22px;
    padding: 0 26px 8px;
    border-bottom: 2px solid var(--paper);
  }
  .services-list {
    list-style: none;
    margin-top: 18px;
    font-weight: 500;
    font-size: 20px;
    line-height: 1.75;
  }
  .services-list li span + span { margin-left: 28px; }

  /* Contact side */
  .card--contact {
    top: 637px;
    background: var(--paper);
  }
  .contact-swoosh { position: absolute; inset: 0; }
  .contact-brand {
    position: absolute;
    left: 60px;
    top: 200px;
    width: 360px;
    display: flex;
    align-items: center;
    gap: 14px;
    color: var(--ink);
    font-weight: 700;
    font-size: 24px;
    line-height: 1.2;
    text-transform: uppercase;
  }
  .contact-brand .mark { width: 22px; height: 22px; flex: none; background: var(--brand-green); }
  .contact-details {
    position: absolute;
    left: 470px;
    top: 60px;
    padding-left: 26px;
    border-left: 2px solid var(--brand-green);
    color: var(--ink);
  }
  .person-name { color: var(--brand-green); font-weight: 700; font-size: 36px; line-height: 1.1; }
  .person-role { font-size: 18px; margin-top: 4px; margin-bottom: 18px; }
  .contact-row {
    display: flex; align-items: center; gap: 12px;
    font-size: 18px; line-height: 1; margin-bottom: 13px;
  }
  .contact-row svg { width: 20px; height: 20px; flex: none; }
</style>
</head>
<body>

<section class="card card--services">
  <div class="services-brand">
    <span class="mark"></span>
    <span>Keystone Homes<small>and Developments Pty Ltd</small></span>
  </div>
  <h2 class="services-title">Our Services</h2>
  <ul class="services-list">
    <li><span>New Homes</span><span>Extensions, Renovations &amp; Bathrooms</span></li>
    <li>Decking, Carports, Sheds (Residential and Industrial)</li>
    <li><span>Carpentry</span><span>Fences, Patios &amp; Pergolas</span></li>
  </ul>
</section>

<section class="card card--contact">
  <svg class="contact-swoosh" viewBox="0 0 860 491" aria-hidden="true">
    <path d="M230 491 C360 400 520 365 690 345 C800 330 845 285 860 245 L860 491 Z" fill="var(--brand-green)"/>
    <path d="M420 372 C620 330 800 335 856 200" fill="none" stroke="var(--brand-green)" stroke-width="5"/>
    <path d="M470 368 C640 342 812 345 858 228" fill="none" stroke="var(--brand-green)" stroke-width="3"/>
  </svg>

  <div class="contact-brand">
    <span class="mark"></span>
    <span>Keystone Homes and Developments Pty Ltd</span>
  </div>

  <div class="contact-details">
    <p class="person-name">Daniel Reeves</p>
    <p class="person-role">Managing Director</p>
    <p class="contact-row">
      <svg viewBox="0 0 20 20"><path d="M5 2l3 4-2 2c1 2.5 3.5 5 6 6l2-2 4 3-2 3C9 18 2 11 2 4z" fill="var(--brand-green)"/></svg>
      555-014-2290
    </p>
    <p class="contact-row">
      <svg viewBox="0 0 20 20"><rect x="2" y="5" width="16" height="11" fill="var(--brand-green)"/><path d="M2 5l8 6 8-6" fill="none" stroke="#fff" stroke-width="1.5"/></svg>
      info@keystonebuild.com
    </p>
    <p class="contact-row">
      <svg viewBox="0 0 20 20"><circle cx="10" cy="10" r="8" fill="var(--brand-green)"/><path d="M2 10h16M10 2c-4 4-4 12 0 16M10 2c4 4 4 12 0 16" fill="none" stroke="#fff" stroke-width="1.2"/></svg>
      www.keystonebuild.com
    </p>
    <p class="contact-row">
      <svg viewBox="0 0 20 20"><circle cx="10" cy="10" r="8" fill="var(--brand-green)"/></svg>
      social.keystonebuild.com
    </p>
  </div>
</section>

</body>
</html>
```